Anesthesia Medical Practice Business Card

We need a business card to hand out to surgeons with my basic information. Something that stands out but is not over the top. The medical community is rather conservative. I'd like them to call me first when flipping through their rolodex of anesthesiologists. I'd like the card to communicate confidence, control, professionalism yet serenity. I don't want the card to be pricey to print.

he logo will be provided as a vector graphic in addition to a complete business card design including the logo

Ravi Pell Okonedo, M.D.
Board Certified Anesthesiologist

(310) 555-0186

rokonedo@mailvane.net

Mailing Address:
48315 Corbel Ave.
Suite 270-4863
Los Angeles, CA 90024

A logo that inegrates my initials perhaps
RO MD
My initials are RO and MD as in Medical Doctor

or
perhaps a physician in surgical mask and cap caring for a patient

Target Market(s)

Surgeons who need anesthesia services

Industry/Entity Type

Medical

Requirements
Must have
• the logo will be provided as a vector graphic in addition to a complete business card design including the logo

Ravi Pell Okonedo, M.D.

(310) 555-0186

rokonedo@mailvane.net

Mailing Address:
48315 Corbel Ave.
Suite 270-4863
Los Angeles, CA 90024

Nice to have
• A logo that inegrates my initials perhaps
RO MD

or

```html
<!DOCTYPE html>
<html lang="en">
<head>
<meta charset="utf-8">
<title>Ravi Pell Okonedo, M.D. — Business Card</title>
<link rel="stylesheet" href="https://fonts.googleapis.com/css2?family=Arimo:wght@400&family=Tinos:wght@400&display=swap">
<style>
  :root {
    --backdrop: #2e2927;
    --card: #f4f4f3;
    --band: #1f8fd6;
    --ink: #1d1d1d;
    --serif: "Tinos", "Times New Roman", serif;
    --sans: "Arimo", Arial, sans-serif;
  }
  * { box-sizing: border-box; margin: 0; padding: 0; }
  html, body { width: 1200px; height: 800px; overflow: hidden; }
  body {
    background: var(--backdrop);
    display: flex;
    align-items: center;
    justify-content: center;
    gap: 40px;
  }
  .card {
    width: 520px;
    height: 297px;
    background: var(--card);
    position: relative;
    box-shadow: 0 6px 18px rgba(0,0,0,.35);
  }
  /* Front */
  .card-front .accent-band {
    position: absolute;
    top: 0; bottom: 0;
    left: 28px;
    width: 112px;
    background: var(--band);
  }
  .contact-block {
    position: absolute;
    left: 150px; right: 14px;
    top: 34px;
    text-align: center;
    color: var(--ink);
  }
  .doctor-name {
    font-family: var(--serif);
    font-size: 22px;
    font-weight: 400;
    letter-spacing: .3px;
    white-space: nowrap;
  }
  .doctor-title {
    font-family: var(--sans);
    font-size: 10.5px;
    margin-top: 2px;
  }
  .contact-list { list-style: none; margin-top: 16px; }
  .contact-item {
    font-family: var(--sans);
    font-size: 11.5px;
    line-height: 1.35;
    margin-bottom: 9px;
    white-space: nowrap;
  }
  .contact-icon {
    display: block;
    margin: 0 auto 4px;
    width: 16px; height: 16px;
    fill: var(--ink);
  }
  /* Back */
  .card-back {
    display: flex;
    align-items: center;
    justify-content: center;
  }
  .practice-name {
    font-family: var(--serif);
    font-size: 30px;
    font-weight: 400;
    color: var(--ink);
    letter-spacing: .5px;
  }
</style>
</head>
<body>
  <section class="card card-front" aria-label="Business card front">
    <div class="accent-band"></div>
    <div class="contact-block">
      <h1 class="doctor-name">Ravi Pell Okonedo, M.D.</h1>
      <p class="doctor-title">Board Certified Anesthesiologist</p>
      <ul class="contact-list">
        <li class="contact-item">
          <svg class="contact-icon" viewBox="0 0 24 24" aria-hidden="true"><path d="M6.6 10.8a15.1 15.1 0 0 0 6.6 6.6l2.2-2.2a1 1 0 0 1 1-.25 11.4 11.4 0 0 0 3.6.57 1 1 0 0 1 1 1V20a1 1 0 0 1-1 1A17 17 0 0 1 3 4a1 1 0 0 1 1-1h3.5a1 1 0 0 1 1 1c0 1.25.2 2.45.57 3.57a1 1 0 0 1-.25 1z"/></svg>
          (310) 555-0186
        </li>
        <li class="contact-item">
          <svg class="contact-icon" viewBox="0 0 24 24" aria-hidden="true"><path d="M2 5h20v14H2zm2 2v.4l8 5.2 8-5.2V7zm0 2.8V17h16V9.8l-8 5.2z"/></svg>
          rokonedo@mailvane.net
        </li>
        <li class="contact-item">
          <svg class="contact-icon" viewBox="0 0 24 24" aria-hidden="true"><path d="M12 2a7 7 0 0 0-7 7c0 5.2 7 13 7 13s7-7.8 7-13a7 7 0 0 0-7-7zm0 9.5A2.5 2.5 0 1 1 12 6.5a2.5 2.5 0 0 1 0 5z"/></svg>
          48315 Corbel Ave. Suite 270-4863<br>Los Angeles, CA 90024
        </li>
      </ul>
    </div>
  </section>

  <section class="card card-back" aria-label="Business card back">
    <span class="practice-name">Ravi Pell Okonedo</span>
  </section>
</body>
</html>
```